50th Invite

Design a 50th birthday invite.

Key essentials to communicate are:

Date: 14 December 2019
Time: 7pm for 7.30pm departure
Birthday person: Glen
Theme: Boat Party
Location: Berth K4 27, Fernquay

Other than that will leave to your creativity. Just for clarity, the above is info to be communicated somehow on the invite, I dont want it to be simply copied.

i would like a luxury boat theme, think Miami, Bahamas etc etc, photos or drawings OK

```html
<!DOCTYPE html>
<html lang="en">
<head>
<meta charset="utf-8">
<title>Glen's 50th Birthday Boat Party</title>
<link rel="stylesheet" href="https://fonts.googleapis.com/css2?family=Bodoni+Moda:ital,wght@0,500;1,700&family=Montserrat:wght@300;700&display=swap">
<style>
  :root {
    --ink: #000000;
    --paper: #ffffff;
    --rule: #d9d9d9;
    --royal: #2e2f8f;
    --royal-deep: #1f1f6e;
    --glow: #3a3db8;
    --silver-light: #f2f2f2;
    --silver-mid: #bdbdbd;
    --silver-dark: #8c8c8c;
  }
  html, body {
    margin: 0;
    padding: 0;
    background: var(--ink);
    overflow: hidden;
  }
  .invite {
    position: relative;
    width: 1109px;
    height: 1200px;
    background: var(--ink);
    overflow: hidden;
    font-family: "Montserrat", sans-serif;
    color: var(--paper);
  }
  .invite__heading {
    position: absolute;
    top: 48px;
    left: 0;
    width: 100%;
    margin: 0;
    text-align: center;
    font-weight: 300;
    font-size: 40px;
    letter-spacing: 2px;
    z-index: 2;
  }
  .invite__top-rule {
    position: absolute;
    top: 119px;
    left: 0;
    width: 100%;
    height: 2px;
    background: var(--rule);
  }
  .invite__artwork {
    position: absolute;
    inset: 0;
  }
  .name-panel {
    position: absolute;
    left: 570px;
    top: 286px;
    width: 486px;
    height: 206px;
    background: linear-gradient(90deg, var(--royal-deep), var(--royal));
    border-top: 2px solid #8a8cd6;
    border-bottom: 2px solid #8a8cd6;
    box-sizing: border-box;
    padding: 20px 0 0 106px;
  }
  .name-panel__name {
    margin: 0;
    font-weight: 300;
    font-size: 84px;
    line-height: 1;
    letter-spacing: 2px;
  }
  .name-panel__occasion {
    margin: 12px 0 0;
    font-weight: 700;
    font-size: 31px;
    line-height: 1.25;
    letter-spacing: 0.5px;
  }
  .yacht {
    position: absolute;
    left: 366px;
    top: 580px;
    width: 680px;
    height: 285px;
    border-radius: 40% 60% 45% 55% / 55% 45% 60% 40%;
    background: radial-gradient(ellipse at 45% 50%, #ffffff 0%, #e6e8ec 45%, rgba(200,205,215,0.6) 70%, rgba(200,205,215,0) 100%);
  }
  .details {
    position: absolute;
    left: 78px;
    top: 911px;
    width: 792px;
  }
  .details__rule {
    height: 3px;
    background: var(--rule);
  }
  .details__text {
    margin: 0;
    padding-left: 67px;
    font-weight: 300;
    font-size: 43px;
    line-height: 54px;
    letter-spacing: 1px;
  }
  .details__when { padding-top: 14px; padding-bottom: 10px; }
  .details__where { padding-top: 12px; padding-bottom: 14px; }
</style>
</head>
<body>
<main class="invite">
  <h1 class="invite__heading">YOU’RE INVITED</h1>
  <div class="invite__top-rule"></div>

  <svg class="invite__artwork" width="1109" height="1200" viewBox="0 0 1109 1200" aria-hidden="true">
    <defs>
      <radialGradient id="blue-glow" cx="0.5" cy="0.5" r="0.5">
        <stop offset="0" stop-color="#3a3db8" stop-opacity="0.95"/>
        <stop offset="0.7" stop-color="#2a2c9a" stop-opacity="0.8"/>
        <stop offset="1" stop-color="#000000" stop-opacity="0"/>
      </radialGradient>
      <linearGradient id="silver" x1="0" y1="0" x2="1" y2="0.3">
        <stop offset="0" stop-color="#bdbdbd"/>
        <stop offset="0.35" stop-color="#f2f2f2"/>
        <stop offset="0.6" stop-color="#8c8c8c"/>
        <stop offset="1" stop-color="#f2f2f2"/>
      </linearGradient>
    </defs>
    <ellipse class="glow" cx="640" cy="730" rx="470" ry="400" fill="url(#blue-glow)"/>
    <text class="numeral numeral--five" x="0" y="0" transform="translate(80 840) scale(1.3 1)" font-family="'Bodoni Moda', serif" font-weight="500" font-size="820" fill="url(#silver)">5</text>
    <text class="numeral numeral--zero" x="0" y="0" transform="translate(455 518) scale(1.3 1)" font-family="'Bodoni Moda', serif" font-weight="500" font-size="470" fill="url(#silver)">0</text>
    <text class="ordinal" x="840" y="226" font-family="'Bodoni Moda', serif" font-style="italic" font-weight="700" font-size="58" fill="#f2f2f2">TH</text>
    <rect class="ordinal-rule" x="828" y="246" width="108" height="3" fill="#d9d9d9"/>
  </svg>

  <section class="name-panel">
    <p class="name-panel__name">GLEN</p>
    <p class="name-panel__occasion">BIRTHDAY<br>BOAT PARTY</p>
  </section>

  <div class="yacht" role="img" aria-label="Photograph of a white luxury motor yacht cruising"></div>

  <section class="details">
    <div class="details__rule"></div>
    <p class="details__text details__when">14 December 2019<br>7pm for 7.30pm departure</p>
    <div class="details__rule"></div>
    <p class="details__text details__where">Berth K4 27, Fernquay</p>
    <div class="details__rule"></div>
  </section>
</main>
</body>
</html>
```